Belmora Wines

Hi all,

My name’s Liam Dowsett and I run a small wine brand based in the Canberra Wine District, Australia. I’m currently in the process of branding the business and am looking for a designer to help develop a new visual direction.

Background
I’ll be growing my own fruit from a leased vineyard site Named 'Wrenhollow' and my family’s property named 'Tibbard Vale', with a stronger emphasis on organic practices and site expression.

The Direction
The brand will centre around single vineyard wines, with each wine reflecting the unique site it comes from. I’d like the branding to support this idea of place, origin, and authenticity.

In terms of visual style, I’m drawn to something that is:

Simple and effective
A balance between traditional and modern
Clean, considered, and not overly decorative

Nothing too over-the-top, the goal is something timeless that lets the wine and vineyard story speak for itself.

At this stage, I’m mainly looking for:

Conceptual design direction / ideas
Label design (with potential to expand into broader branding)

I’m open to creative interpretation, so if the story resonates with you, I’d love to see how you would approach it.

Below I've attached an example of the bottle shape I will be using.

Cheers,
Liam

Colors
0054AA
0677BA
7BADD7
CADEEF
E8F1F8
FFC000
F8CF3A
FAE287
FDF2CF
FEFAEE

Requirements
Must have
• Mix of modern and traditional

```html
<!DOCTYPE html>
<html lang="en">
<head>
<meta charset="utf-8">
<title>Belmora Riesling – Label</title>
<link href="https://fonts.googleapis.com/css2?family=Marcellus&family=Pinyon+Script&family=Open+Sans:wght@400&display=swap" rel="stylesheet">
<style>
  :root {
    --page-bg: #fbf8f4;
    --label-light: #fffdf5;
    --label-warm: #fdf2d9;
    --ink: #111111;
    --ink-soft: #5a5a5a;
    --ink-faint: #b8b8b8;
    --vine-green: #6c9a1e;
    --mark-green: #3f8a1c;
  }
  html, body {
    margin: 0;
    padding: 0;
    width: 1200px;
    height: 3204px;
    overflow: hidden;
    background: var(--page-bg);
  }
  .canvas {
    position: relative;
    width: 1200px;
    height: 3204px;
  }
  .label {
    position: absolute;
    left: 100px;
    top: 875px;
    width: 1000px;
    height: 1453px;
    background: linear-gradient(90deg, var(--label-light) 0%, var(--label-light) 45%, var(--label-warm) 100%);
    box-shadow: 0 0 0 1px rgba(0,0,0,0.04);
  }
  .label > * {
    position: absolute;
    left: 0;
    right: 0;
    margin: 0;
    text-align: center;
  }
  .vintage {
    top: 96px;
    font-family: "Open Sans", sans-serif;
    font-size: 38px;
    letter-spacing: 0.18em;
    color: var(--ink);
  }
  .brand-mark {
    top: 468px;
    left: 385px;
    right: auto;
    width: 230px;
    height: 230px;
  }
  .variety {
    top: 860px;
    font-family: "Pinyon Script", cursive;
    font-size: 96px;
    line-height: 1;
    color: var(--vine-green);
  }
  .brand-name {
    top: 1010px;
    font-family: "Marcellus", serif;
    font-size: 150px;
    line-height: 1;
    letter-spacing: 0.04em;
    color: var(--ink);
  }
  .district {
    top: 1172px;
    font-family: "Open Sans", sans-serif;
    font-size: 24px;
    letter-spacing: 0.42em;
    color: var(--ink-soft);
  }
  .district .region { color: var(--ink-faint); }
  .country {
    top: 1320px;
    font-family: "Open Sans", sans-serif;
    font-size: 38px;
    letter-spacing: 0.45em;
    color: var(--ink-soft);
  }
</style>
</head>
<body>
  <main class="canvas">
    <section class="label">
      <p class="vintage">2026</p>
      <svg class="brand-mark" viewBox="0 0 230 230" aria-hidden="true">
        <circle cx="115" cy="115" r="112" fill="var(--mark-green)"/>
      </svg>
      <p class="variety">Riesling</p>
      <h1 class="brand-name">BELMORA</h1>
      <p class="district"><span class="region">CANBERRA</span> WINE DISTRICT</p>
      <p class="country">AUSTRALIA</p>
    </section>
  </main>
</body>
</html>
```